MORVETH ELECTRICAL CONTRACTING - Electrical business

I need a design to go over a new van.
It needs to include;
The logo (All over, you decide)
phone number - 0417362850 (large)
email - kieran@morvethelectrical.example (medium)
website - www.morvethelectrical.example (small)
EC number - EC58216 (small)
"DOMESTIC & COMMERCIAL" (medium)
The facebook and instagram logos

I have uploaded the new van
my 2 logos
my existing ute as an idea
and a friends ute as another idea (sharp)

```html
<!DOCTYPE html>
<html lang="en">
<head>
<meta charset="utf-8">
<title>Morveth Electrical Contracting – Van Side Wrap</title>
<link rel="stylesheet" href="https://fonts.googleapis.com/css2?family=Roboto+Condensed:wght@400;500&display=swap">
<style>
  :root {
    --canvas-bg-top: #a9abab;
    --canvas-bg-bottom: #eeeeee;
    --wrap-white: #f4f4f2;
    --brand-red: #d71920;
    --brand-red-deep: #b5121a;
    --ink: #231f20;
  }
  html, body {
    margin: 0;
    padding: 0;
    width: 1200px;
    height: 1200px;
    overflow: hidden;
  }
  body {
    background: linear-gradient(180deg, var(--canvas-bg-top) 0%, var(--canvas-bg-bottom) 60%, #f7f7f7 100%);
    font-family: "Roboto Condensed", "Arial Narrow", sans-serif;
    color: var(--ink);
    position: relative;
  }
  .wrap-panel {
    position: absolute;
    left: 60px;
    top: 390px;
    width: 1080px;
    height: 400px;
    border-radius: 28px;
    overflow: hidden;
    background: var(--wrap-white);
    box-shadow: 0 18px 30px rgba(0,0,0,0.18);
  }
  .wrap-graphic {
    position: absolute;
    inset: 0;
  }
  .brand-block {
    position: absolute;
    left: 595px;
    top: 36px;
    width: 320px;
    display: flex;
    flex-direction: column;
    align-items: center;
    color: var(--brand-red);
    font-weight: 500;
    line-height: 1;
    text-transform: uppercase;
  }
  .brand-mark {
    width: 52px;
    height: 52px;
    background: var(--brand-red);
  }
  .brand-main {
    margin-top: 10px;
    font-size: 38px;
    letter-spacing: 9px;
    padding-left: 9px;
  }
  .brand-sub {
    margin-top: 6px;
    font-size: 15px;
    letter-spacing: 5.6px;
    padding-left: 5.6px;
  }
  .social-row {
    position: absolute;
    left: 597px;
    top: 180px;
    display: flex;
    align-items: center;
    gap: 10px;
    font-size: 20px;
    font-weight: 500;
    line-height: 1;
    color: var(--brand-red);
  }
  .social-square {
    width: 24px;
    height: 24px;
    border-radius: 4px;
    background: var(--brand-red);
  }
  .contact-block {
    position: absolute;
    left: 273px;
    top: 180px;
    line-height: 1;
  }
  .contact-phone {
    font-size: 50px;
    font-weight: 400;
    letter-spacing: 0.5px;
    margin: 0;
  }
  .contact-email {
    font-size: 21px;
    margin: 6px 0 0;
  }
  .contact-web {
    font-size: 14.5px;
    margin: 5px 0 0;
  }
  .contact-ec {
    font-size: 14.5px;
    margin: 4px 0 0 100px;
  }
  .contact-services {
    font-size: 20px;
    margin: 8px 0 0 72px;
    text-transform: uppercase;
  }
</style>
</head>
<body>
  <section class="wrap-panel" aria-label="Van side wrap design">
    <svg class="wrap-graphic" viewBox="0 0 1080 400" width="1080" height="400" aria-hidden="true">
      <path d="M0 315 C 120 330, 230 352, 380 350 C 520 346, 600 320, 680 290"
            fill="none" stroke="var(--brand-red)" stroke-width="6"/>
      <path d="M0 355 C 150 372, 300 388, 440 372 C 600 352, 700 290, 820 215 C 900 168, 990 142, 1080 138 L 1080 400 L 0 400 Z"
            fill="var(--brand-red)"/>
      <path d="M0 385 C 250 400, 500 392, 700 350 C 860 316, 980 300, 1080 300 L 1080 400 L 0 400 Z"
            fill="var(--brand-red-deep)" opacity="0.55"/>
    </svg>

    <div class="brand-block">
      <span class="brand-mark" aria-hidden="true"></span>
      <span class="brand-main">Morveth</span>
      <span class="brand-sub">Electrical Contracting</span>
    </div>

    <div class="social-row">
      <span class="social-square" aria-hidden="true"></span>
      <span class="social-handle">@morvethelectrical</span>
    </div>

    <div class="contact-block">
      <p class="contact-phone">0417362850</p>
      <p class="contact-email">email - kieran@morvethelectrical.example</p>
      <p class="contact-web">website - www.morvethelectrical.example</p>
      <p class="contact-ec">EC number - EC58216</p>
      <p class="contact-services">Domestic &amp; Commercial</p>
    </div>
  </section>
</body>
</html>
```